Hospital Website Design - PSD only

We need a web design for a community hospital based in Uniontown, Pennsylvania.

We would like to see a first round of designs for the website HOMEPAGE. Once we have selected finalists for the look & feel, based on the submitted homepage designs, we will request an additional INTERNAL page design.

Both designs should follow the content requirements displayed on the attached wireframes. I will post the internal page wireframe after the homepage design finalists are selected.

The desired Look & Feel for the website is clean and modern.

3 sites we like are:
http://www.marvellcare.org/
http://www.qrtm.org/
http://www.dellwyn.org/

Attached are the Homepage wireframe, and the Brackfield Hospital Logo.

The winning design will communicate a bright, healthy, energetic, community-oriented feeling.

Please note that readability is very important for a hospital website. Font-sizes and line-heights should be carefully selected for comfortable reading.
Updates

Dear designers -- Please don't feel locked into the exact shades of blue / brown used in the logo. We find this color scheme quite ugly and are working on a logo update. The new color scheme will probably still involve some shades of blue and brown, but we aren't sure yet. Please use your best judgement to make a beautiful design, similar in style to the modern / simple aesthetic of http://www.marvellcare.org/ We will be working on feedback to designs today. Thank you.

Regarding Large Rotating Graphic area and Navigation: We prefer a full-width display, rather than boxed. The navigation should be visually prominent, easy to read text that one can scan easily across the top of the page. Again, please refer to http://www.marvellcare.org/ for our preferred design aesthetic. Some of the designs submitted have been somewhat dated in their styling. We'd like a polished, modern, crisp, bold, beautiful design.

Re: choice of image in large rotating graphic area -- Designers, please do not use stock photography of a group of doctors, or a nursing home scene, in your sample rotating graphic areas. Although this should not affect our perception of the design, it throws off everything in the page if we don't like the image. Please try to select a bold / attractive image that you would like to set the tone for your design.

Reason: Extending our deadline to receive more designs exploring other color options containing less brown, or browns with a more attractive vibe. We would also like to see designs that are not exact replicas of the wireframe. The wireframe is just to show the elements on the page. Please use your creativity to utilize these elements in an attractive layout that we will like. We would also prefer to see use of photography that shows a younger, more cheerful, hopeful feeling in the design... and where the photographs are consistent with your design approach. Thanks!

In general, feedback for everyone is, please look here: http://www.marvellcare.org/ that's the feeling / vibe we want. DO NOT let the old, ugly, outdated logo determine your design. We are having the logo redesigned. DO NOT take an ugly, outdated template, and adapt it for this website. We want to see something BEAUTIFUL!!! Please give us your best effort! People who come to this website are in health crisis, and they want to be uplifted!! Their good spirits are in your hands.

Reason: We are still reviewing submissions and working with designers to provide better feedback. Thanks for your patience.

Reason: our sincerest apologies for the failure to provide adequate feedback this week. We hit a snag with the various decision makers on this project and were not able to review the recent submissions. We will make every effort to have a decision by tomorrow. Thank you for your patience.

Target Market(s)

Adults based in suburban & rural community, aged 18-80.

Industry/Entity Type

Hospital

Requirements
Must have
• The design must include all of the content areas outlined on the attached wireframe.
The design must include the attached logo. (Note, we may update the logo during the design contest, but it will not be changed dramatically. It will just be modernized slightly.)
Nice to have
• Show hover states for things like Navigation, Links, or small images in gallery, so we can see how you imagine interactive states.

```html
<!DOCTYPE html>
<html lang="en">
<head>
<meta charset="utf-8">
<title>Brackfield Hospital – Footer</title>
<link rel="stylesheet" href="https://fonts.googleapis.com/css2?family=Gelasio:ital,wght@0,400;0,600;1,400&display=swap">
<style>
:root{
  --ink:#3b3b3b;
  --heading:#666;
  --muted:#9a9a9a;
  --rule:#9c9c9c;
  --dash:#dcdcdc;
  --link:#1f5ca8;
  --hover-bg:#dde4ee;
  --icon:#3d3d3d;
  --navy:#0c1f66;
  --navy-line:#1b2f70;
  --thumb:#222;
  --ribbon:#1b78c4;
  --ribbon-dark:#0f4f8f;
  --ribbon-face:#2a64a8;
}
*{box-sizing:border-box;margin:0;padding:0}
html,body{width:1200px;height:676px;overflow:hidden;background:#fff}
body{position:relative;font-family:"Gelasio",Georgia,serif;color:var(--ink)}
a{text-decoration:none;color:inherit}
.col{position:absolute;top:38px}
.col-title{font-size:22px;font-weight:400;color:var(--heading);padding-bottom:4px;border-bottom:1px solid var(--rule);line-height:28px}
.news{left:120px;width:313px}
.events{left:469px;width:291px}
.visit{left:793px;width:285px}

.news-item{position:relative;height:91px;border-bottom:1px dashed var(--dash)}
.news-list{margin-top:15px}
.news-thumb{position:absolute;left:3px;top:8px;width:58px;height:62px;background:var(--thumb);border:2px solid #e6e6e6;box-shadow:0 0 0 1px #ccc}
.news-text{position:absolute;left:81px;top:14px;font-size:13.5px;line-height:20px;width:235px}
.date{font-style:italic;font-size:12.5px;color:var(--muted)}
.news-item .date{position:absolute;left:79px;top:56px}
.more{display:block;font-size:13px;font-weight:600;color:var(--link);margin-top:12px;padding-left:5px}

.event{border-bottom:1px solid #d0d0d0;padding:18px 0 14px 2px}
.event-title{font-size:13.5px;line-height:20px}
.event .date{display:block;margin-top:1px;margin-left:-2px}
.event-excerpt{font-size:12.5px;line-height:18px;margin-top:9px}
.events .more{margin-top:46px;padding-left:2px}

.visit-list{list-style:none;margin-top:14px}
.visit-list li{height:39px;display:flex;align-items:center;font-size:15.5px}
.visit-list svg{width:24px;height:24px;margin-right:14px;fill:var(--icon)}
.visit-list .active{background:var(--hover-bg);color:var(--link);padding-left:10px;margin-left:2px;height:35px;margin-top:2px;margin-bottom:2px}
.visit-list .active svg{fill:var(--link);width:22px;margin-right:16px}

.divider{position:absolute;left:0;top:493px;width:1200px;height:3px;background:var(--navy-line)}
.footer-links{position:absolute;left:121px;top:532px;width:430px;font-size:15.5px;line-height:26px;color:#555}
.footer-links .sep{margin:0 11px;color:#777}
.follow{position:absolute;left:627px;top:526px;width:140px;text-align:center;font-size:16px;color:#444}
.social{display:flex;gap:8px;justify-content:center;margin-top:8px}
.social span{width:27px;height:27px;border-radius:50%;background:#444;display:block}
.awards{position:absolute;left:855px;top:518px}
.bottom-bar{position:absolute;left:0;top:622px;width:1200px;height:54px;background:var(--navy);color:#fff;font-size:13.5px}
.copyright{position:absolute;left:120px;top:19px}
.legal{position:absolute;right:122px;top:19px}
.legal .sep{margin:0 7px;opacity:.8}
</style>
</head>
<body>

<section class="col news">
  <h2 class="col-title">BH News</h2>
  <div class="news-list">
    <article class="news-item"><div class="news-thumb" role="img" aria-label="News story thumbnail photo"></div><p class="news-text">Lorem ipsum dolor sit amtet, consect etur adipiscing elit.</p><span class="date">September 14, 2014</span></article>
    <article class="news-item"><div class="news-thumb" role="img" aria-label="News story thumbnail photo"></div><p class="news-text">Lorem ipsum dolor sit amet, consect etur adipiscing elit.</p><span class="date">September 14, 2014</span></article>
    <article class="news-item"><div class="news-thumb" role="img" aria-label="News story thumbnail photo"></div><p class="news-text">Lorem ipsum dolor sit amet, consect etur adipiscing elit.</p><span class="date">September 14, 2014</span></article>
    <article class="news-item"><div class="news-thumb" role="img" aria-label="News story thumbnail photo"></div><p class="news-text">Lorem ipsum dolor sit amet, consect etur adipiscing elit.</p><span class="date">September 14, 2014</span></article>
  </div>
  <a class="more" href="#">VIEW MORE »</a>
</section>

<section class="col events">
  <h2 class="col-title">Upcoming Classes &amp; Events</h2>
  <article class="event">
    <p class="event-title">Lorem ipsum dolor sit amet, consectetur adipiscing elit.</p>
    <span class="date">September 14, 2014</span>
    <p class="event-excerpt">“ Lorem ipsum dolor sit amet, consectetur adipi-scing elit. Nunc non diam “ Lorem ipsum dolor sit amet, consectetur adipiscing elit. Nunc non diam “ Lorem ipsum dolor sit amet,</p>
  </article>
  <article class="event">
    <p class="event-title">Lorem ipsum dolor sit amet, consectetur adipiscing elit.</p>
    <span class="date">September 14, 2014</span>
    <p class="event-excerpt">“ Lorem ipsum dolor sit amet, consectetur adipi-scing elit. Nunc non diam “ Lorem ipsum dolor sit amet, consectetur adipiscing elit. Nunc non diam “ Lorem ipsum dolor sit amet</p>
  </article>
  <a class="more" href="#">VIEW MORE »</a>
</section>

<section class="col visit">
  <h2 class="col-title">About Your Visit</h2>
  <ul class="visit-list">
    <li><svg viewBox="0 0 24 24"><rect x="1" y="5" width="22" height="18" rx="2"/><rect x="8" y="1" width="8" height="5" rx="1" fill="none" stroke="#3d3d3d" stroke-width="2"/><path d="M10.5 9h3v3.5H17v3h-3.5V19h-3v-3.5H7v-3h3.5z" fill="#fff"/></svg>Emergency Care</li>
    <li><svg viewBox="0 0 24 24"><path d="M2 3h14v6l-2 2V5H4v16h10v-3l2-2v7H2z"/><path d="M6 8h7v1.6H6zM6 12h5v1.6H6zM9 18l3-1 10-10-2-2L10 15z"/></svg>Accepted Health Plans</li>
    <li><svg viewBox="0 0 24 24"><path d="M4 3h4V1h8v2h4v21H4zM6 5v17h12V5h-2v2H8V5z"/><path d="M8 10h8v1.5H8zM8 13.5h8V15H8zM8 17h8v1.5H8z"/></svg>Pre-registration for Surgery</li>
    <li><svg viewBox="0 0 24 24"><path d="M8 1h4v2h-1v6l-6 11h8v2H2l7-13V3H8z"/><circle cx="16" cy="16" r="7" fill="none" stroke="#3d3d3d" stroke-width="2"/><path d="M15 12h2v4h3v2h-5z"/></svg>Lab Hours</li>
    <li class="active"><svg viewBox="0 0 24 24"><path d="M2 4h4V2h2v2h8V2h2v2h4v19H2zM4 9v12h16V9z"/><path d="M6 11h2.5v2H6zM10.7 11h2.5v2h-2.5zM15.5 11H18v2h-2.5zM6 14.5h2.5v2H6zM10.7 14.5h2.5v2h-2.5zM15.5 14.5H18v2h-2.5zM6 18h2.5v2H6zM10.7 18h2.5v2h-2.5z"/></svg>Schedule a Lab Test</li>
    <li><svg viewBox="0 0 24 24"><rect x="2" y="3" width="6" height="19" rx="2"/><path d="M9 5h13v17H9v-2h11V7H9z"/><path d="M12 9h2v2h-2zM15.5 9h2v2h-2zM12 12.5h2v2h-2zM15.5 12.5h2v2h-2zM12 16h2v2h-2zM15.5 16h2v2h-2z"/></svg>Find a Phone Number</li>
    <li><svg viewBox="0 0 24 24"><path d="M2 4h12l-2 2H4v14h14v-8l2-2v12H2z"/><path d="M8 16l1-4L20 1l3 3-11 11z"/></svg>Find a Form</li>
    <li><svg viewBox="0 0 24 24"><rect x="1" y="3" width="22" height="13" rx="1"/><circle cx="12" cy="9.5" r="4" fill="#fff"/><path d="M11.3 7h1.4v5h-1.4z"/><path d="M9 18h6v1h-2v4h-2v-4H9z"/></svg>Pay Bill Online</li>
    <li><svg viewBox="0 0 24 24"><rect x="2" y="2" width="20" height="20" rx="2"/><path d="M9 9.5a3 3 0 1 1 4.5 2.5c-1 .6-1.5 1-1.5 2.5" fill="none" stroke="#fff" stroke-width="2.2"/><circle cx="12" cy="18" r="1.4" fill="#fff"/></svg>Visitor Guide</li>
  </ul>
</section>

<div class="divider"></div>

<nav class="footer-links">
  <a href="#">Referring Physicians</a><span class="sep">|</span><a href="#">Medical Professionals</a><span class="sep">|</span><a href="#">Giving</a><br>
  <span class="sep" style="margin-left:0">|</span><a href="#">Volunteering</a><span class="sep">|</span><a href="#">Career</a><span class="sep">|</span><a href="#">Online Bill Pay</a>
</nav>

<div class="follow">
  <p>Follow us on:</p>
  <div class="social"><span aria-label="Social network one"></span><span aria-label="Social network two"></span><span aria-label="Social network three"></span><span aria-label="Social network four"></span></div>
</div>

<svg class="awards" width="222" height="82" viewBox="0 0 222 82" aria-label="Awards">
  <defs><linearGradient id="shade" x1="0" y1="0" x2="0" y2="1"><stop offset="0" stop-color="#000" stop-opacity=".25"/><stop offset="1" stop-color="#000" stop-opacity="0"/></linearGradient></defs>
  <ellipse cx="111" cy="74" rx="100" ry="8" fill="url(#shade)"/>
  <path d="M8 18h52v52H8l-7-26z" fill="var(--ribbon)"/>
  <path d="M214 18h-52v52h52l7-26z" fill="var(--ribbon)"/>
  <path d="M38 52h22v18z M184 52h-22v18z" fill="var(--ribbon-dark)"/>
  <rect x="38" y="2" width="146" height="56" fill="var(--ribbon)"/>
  <rect x="42" y="6" width="138" height="48" fill="var(--ribbon-face)" stroke="#5fa6e0" stroke-width="1.5"/>
  <text x="111" y="35" text-anchor="middle" fill="#fff" font-family="Gelasio, Georgia, serif" font-size="17">AWARDS</text>
</svg>

<footer class="bottom-bar">
  <p class="copyright">© Copyright 2014 Brackfield Hospital. All Rights Reserved.</p>
  <p class="legal"><a href="#">Privacy Policy</a><span class="sep">|</span><a href="#">Terms &amp; Conditions</a></p>
</footer>

</body>
</html>
```